Automobile Review website Requires a stunning Design

Automobiles are an essential part of life and other day-to-day activities and in this vein we are starting up a business website which deal on review of different Automobiles (ranging from cars, trucks, suv, pick up).
The website have to be a "one stop place" for buyers. Our website name is Motor Verdict Hub
Our taste: We dislike template. The design should have some unique elements which helps to distinguish us from competitors. Designs should make a logo along with design.
Required pages:
1. Home - Search cars, News, Reviews, Comparison, Featured cars.
2. Car and Model - This comprises of different cars make, models and features
3. Review page - Detailed analysis and discussions about the different make and model of cars.
NB: We would like to see a mobile size design for the homepage.

```html
<!DOCTYPE html>
<html lang="en">
<head>
<meta charset="utf-8">
<title>Motor Verdict Hub – Mobile Home</title>
<link href="https://fonts.googleapis.com/css2?family=Nunito+Sans:ital,wght@0,400;0,600;0,700;1,400&display=swap" rel="stylesheet">
<style>
:root{
  --page:#eeeef2;
  --blue:#2a6fd6;
  --blue-light:#6fa0ea;
  --green:#2f7a12;
  --green-dark:#0f3a08;
  --ink:#333;
  --muted:#9a9a9a;
  --grey-band:#ececec;
  --white:#fff;
  --footer:#141414;
}
*{box-sizing:border-box;margin:0;padding:0}
html,body{width:1200px;height:3651px;overflow:hidden}
body{background:var(--page);font-family:"Nunito Sans",Arial,sans-serif;color:var(--ink)}
.screen{width:960px;margin:25px auto 0;background:var(--white);position:relative}

/* header */
.app-header{height:110px;background:var(--blue);display:flex;align-items:center;justify-content:space-between;padding:0 40px}
.menu-toggle{width:60px;display:flex;flex-direction:column;gap:9px}
.menu-toggle span{height:4px;background:var(--blue-light);border-radius:2px}
.brand{color:var(--white);font-size:40px;font-weight:600}

/* hero */
.hero{height:455px;position:relative;overflow:hidden}
.hero-photo{position:absolute;inset:0;background:linear-gradient(180deg,#8a5a34 0%,#c0823f 28%,#5b3b28 55%,#2b2420 100%)}
.hero-title{position:absolute;top:228px;left:0;right:0;text-align:center;color:var(--white);font-size:46px;font-weight:600;top:120px}
.hero-search{position:absolute;top:212px;left:157px;width:668px;height:69px;display:flex;background:var(--white)}
.hero-search input{flex:1;border:0;padding:0 28px;font:400 22px "Nunito Sans",sans-serif;color:#777;outline:none}
.hero-search button{width:78px;border:0;background:var(--blue);display:flex;align-items:center;justify-content:center}
.slider-dashes{position:absolute;top:420px;left:0;right:0;display:flex;justify-content:center;gap:14px}
.slider-dashes span{width:34px;height:5px;background:var(--white);opacity:.9}

/* categories */
.categories{height:213px;display:flex;background:linear-gradient(180deg,#2c6a14 0%,var(--green-dark) 100%)}
.category{flex:1;display:flex;flex-direction:column;align-items:center;justify-content:flex-end;padding-bottom:42px;gap:26px;color:var(--white);font-size:22px;border-right:2px solid rgba(0,0,0,.35)}
.category:last-child{border-right:0}

/* featured */
.featured{height:769px;padding-top:70px}
.section-title{text-align:center;font-size:46px;font-weight:600}
.featured .section-title{color:var(--green)}
.card-row{display:flex;gap:19px;padding:0 35px 0 31px;margin-top:36px}
.car-card{width:436px;height:511px;border:2px solid #ddd;background:var(--white)}
.car-photo{height:289px}
.car-photo.dark-suv{background:linear-gradient(135deg,#c08a2c,#3a2f22 60%,#6f6a60)}
.car-photo.blue-sedan{background:linear-gradient(135deg,#3a4a55,#1d2d55 55%,#6b7a85)}
.car-body{padding:22px 36px}
.car-title{font-size:28px;font-weight:600;color:#444}
.car-text{font-size:19px;color:var(--muted);line-height:1.45;margin-top:8px}
.car-footer{display:flex;justify-content:space-between;align-items:center;margin-top:18px}
.price{font-size:38px;color:var(--blue);font-weight:600}
.btn-outline{border:2px solid var(--blue);color:var(--blue);border-radius:30px;font-size:16px;font-weight:700;padding:11px 22px}
.dots{display:flex;justify-content:center;gap:10px}
.dots span{width:18px;height:18px;border-radius:50%;background:#ccc}
.dots span:first-child{background:var(--white);border:2px solid #bbb}
.featured .dots{margin-top:40px}

/* comparison */
.comparison{height:784px;background:var(--grey-band);padding-top:56px}
.compare-card{position:relative;margin:36px 37px 0;height:518px;background:var(--white);box-shadow:0 4px 18px rgba(0,0,0,.18);text-align:center}
.compare-cars{position:absolute;top:95px;left:60px;width:720px;height:190px;display:flex;align-items:center;justify-content:space-between}
.compare-car{width:330px;height:180px;border-radius:80px 90px 30px 30px}
.compare-car.blue{background:linear-gradient(180deg,#3a63c8,#1d3f9a)}
.compare-car.white{background:linear-gradient(180deg,#f4f4f4,#cfcfcf)}
.vs-badge{position:absolute;left:345px;top:60px;width:50px;height:50px;background:#111;transform:rotate(45deg);display:flex;align-items:center;justify-content:center}
.vs-badge span{transform:rotate(-45deg);color:var(--white);font-size:18px;font-weight:700}
.compare-title{position:absolute;top:325px;left:0;right:0;color:var(--green);font-size:30px;font-weight:700}
.compare-text{position:absolute;top:370px;left:90px;right:90px;color:var(--muted);font-size:21px;line-height:1.4}
.btn-solid{position:absolute;bottom:-34px;left:50%;transform:translateX(-50%);width:223px;height:69px;border-radius:35px;background:var(--blue);color:var(--white);font-size:20px;font-weight:700;display:flex;align-items:center;justify-content:center}
.comparison .dots{margin-top:74px}

/* reviews */
.reviews{height:424px;background:linear-gradient(90deg,#2e7f1c 0%,#2a8055 45%,#2a6fd6 100%);color:var(--white);position:relative;text-align:center;padding-top:58px}
.reviews .section-title{font-size:40px}
.quote{margin:30px auto 0;width:720px;font-size:21px;font-style:italic;line-height:1.55;opacity:.85}
.quote-mark{font-size:40px;font-weight:700;font-style:normal;vertical-align:-8px;opacity:.7}
.review-arrow{position:absolute;top:160px}
.review-arrow.prev{left:28px}
.review-arrow.next{right:28px}
.author{display:flex;align-items:center;justify-content:center;gap:16px;margin-top:22px;text-align:left}
.avatar{width:80px;height:80px;border-radius:50%;background:#b9a08a;border:4px solid var(--white)}
.author-name{font-size:22px;font-weight:600}
.author-city{font-size:16px;opacity:.85}

/* news */
.news{height:596px;padding:48px 46px 0 47px}
.news-head{display:flex;justify-content:space-between;align-items:center}
.news-head h2{font-size:40px;font-weight:600}
.news-arrows{display:flex;gap:18px}
.news-row{display:flex;gap:38px;margin-top:32px}
.news-item{width:414px}
.news-photo{height:229px}
.news-photo.lineup{background:linear-gradient(180deg,#6c6f75 0%,#8a8d92 50%,#8d3b38 75%,#7a7a78 100%)}
.news-photo.drivers{background:linear-gradient(135deg,#d9c7a8,#8a6a4c 50%,#c9b7a0)}
.news-title{font-size:27px;font-weight:600;margin-top:26px}
.news-text{font-size:22px;line-height:1.4;color:#444;margin-top:6px}
.read-more{font-size:21px;font-weight:700;color:var(--green);margin-top:4px}

/* footer */
.site-footer{height:251px;background:var(--footer);color:#ddd;text-align:center;padding-top:58px;font-size:20px}
.footer-links{color:#aaa;margin-top:10px}
.social{display:flex;justify-content:center;gap:10px;margin-top:22px}
.social span{width:44px;height:44px;border-radius:50%;border:2px solid #ddd}
</style>
</head>
<body>
<main class="screen">
  <header class="app-header">
    <div class="menu-toggle" aria-label="Menu"><span></span><span></span><span></span></div>
    <div class="brand">Motor Verdict Hub</div>
    <svg width="40" height="40" viewBox="0 0 40 40" aria-label="Search"><circle cx="17" cy="17" r="11" fill="none" stroke="#a9c6f2" stroke-width="4"/><line x1="25" y1="25" x2="35" y2="35" stroke="#a9c6f2" stroke-width="5" stroke-linecap="round"/></svg>
  </header>

  <section class="hero">
    <div class="hero-photo" role="img" aria-label="Photo of a person leaning out of a car on an open road at sunset"></div>
    <h1 class="hero-title">SEARCH CARS HERE</h1>
    <form class="hero-search">
      <input type="text" placeholder="Type your Car here" aria-label="Search cars">
      <button type="button" aria-label="Search"><svg width="32" height="32" viewBox="0 0 32 32"><circle cx="13" cy="13" r="9" fill="none" stroke="#fff" stroke-width="4"/><line x1="20" y1="20" x2="28" y2="28" stroke="#fff" stroke-width="4" stroke-linecap="round"/></svg></button>
    </form>
    <div class="slider-dashes"><span></span><span></span><span></span></div>
  </section>

  <nav class="categories">
    <div class="category">
      <svg width="150" height="56" viewBox="0 0 150 56"><path d="M6 40 V30 Q8 24 20 22 L48 18 Q62 6 86 6 Q106 6 120 20 L138 24 Q146 26 146 34 V40 Z" fill="#fff"/><circle cx="38" cy="42" r="10" fill="#1c4a0c" stroke="#fff" stroke-width="4"/><circle cx="114" cy="42" r="10" fill="#1c4a0c" stroke="#fff" stroke-width="4"/></svg>
      CARS
    </div>
    <div class="category">
      <svg width="120" height="66" viewBox="0 0 120 66"><rect x="34" y="4" width="82" height="44" fill="#fff"/><path d="M4 48 V30 L14 16 H30 V48 Z" fill="#fff"/><circle cx="24" cy="52" r="9" fill="#1c4a0c" stroke="#fff" stroke-width="4"/><circle cx="96" cy="52" r="9" fill="#1c4a0c" stroke="#fff" stroke-width="4"/></svg>
      TRUCKS
    </div>
    <div class="category">
      <svg width="150" height="60" viewBox="0 0 150 60"><path d="M6 44 V26 Q8 20 18 18 L36 6 H110 L132 20 Q144 22 144 32 V44 Z" fill="none" stroke="#fff" stroke-width="4"/><path d="M44 12 H72 V22 H34 Z M78 12 H106 L116 22 H78 Z" fill="#fff"/><circle cx="40" cy="46" r="9" fill="#1c4a0c" stroke="#fff" stroke-width="4"/><circle cx="112" cy="46" r="9" fill="#1c4a0c" stroke="#fff" stroke-width="4"/></svg>
      SUV
    </div>
    <div class="category">
      <svg width="150" height="60" viewBox="0 0 150 60"><path d="M6 44 V28 H70 V10 Q96 8 104 24 L136 28 Q144 30 144 38 V44 Z" fill="none" stroke="#fff" stroke-width="4"/><path d="M78 16 H96 L102 26 H78 Z" fill="#fff"/><circle cx="36" cy="46" r="9" fill="#1c4a0c" stroke="#fff" stroke-width="4"/><circle cx="116" cy="46" r="9" fill="#1c4a0c" stroke="#fff" stroke-width="4"/></svg>
      PICK UP
    </div>
  </nav>

  <section class="featured">
    <h2 class="section-title">Featured Cars</h2>
    <div class="card-row">
      <article class="car-card">
        <div class="car-photo dark-suv" role="img" aria-label="Photo of a dark SUV on an autumn road"></div>
        <div class="car-body">
          <h3 class="car-title">Car/Brand Tittle here</h3>
          <p class="car-text">Mauris neque metus malesuada nec ultricies sit amet porttitor mattis</p>
          <div class="car-footer"><span class="price">$125.99</span><span class="btn-outline">VIEW DETAILS</span></div>
        </div>
      </article>
      <article class="car-card">
        <div class="car-photo blue-sedan" role="img" aria-label="Photo of a blue sedan driving fast"></div>
        <div class="car-body">
          <h3 class="car-title">Car/Brand Tittle here</h3>
          <p class="car-text">Mauris neque metus malesuada nec ultricies sit amet porttitor mattis</p>
          <div class="car-footer"><span class="price">$125.99</span><span class="btn-outline">VIEW DETAILS</span></div>
        </div>
      </article>
    </div>
    <div class="dots"><span></span><span></span><span></span><span></span></div>
  </section>

  <section class="comparison">
    <h2 class="section-title">Comparison</h2>
    <article class="compare-card">
      <div class="compare-cars">
        <div class="compare-car blue" role="img" aria-label="Photo of a blue sedan"></div>
        <div class="vs-badge"><span>VS</span></div>
        <div class="compare-car white" role="img" aria-label="Photo of a white sedan"></div>
      </div>
      <h3 class="compare-title">Car/Brand vs Cars Tittle here</h3>
      <p class="compare-text">Mauris neque metus malesuada nec ultricies sit amet porttitor mattis enim in massa libero interdum nec</p>
      <span class="btn-solid">LEARN MORE</span>
    </article>
    <div class="dots"><span></span><span></span><span></span><span></span></div>
  </section>

  <section class="reviews">
    <h2 class="section-title">Reviews</h2>
    <svg class="review-arrow prev" width="24" height="70" viewBox="0 0 24 70"><polyline points="20,4 4,35 20,66" fill="none" stroke="#fff" stroke-width="2" opacity=".7"/></svg>
    <svg class="review-arrow next" width="24" height="70" viewBox="0 0 24 70"><polyline points="4,4 20,35 4,66" fill="none" stroke="#fff" stroke-width="2" opacity=".7"/></svg>
    <p class="quote"><span class="quote-mark">“</span> Mauris neque metus malesuada nec ultricies sit amet porttitor mattis enim in massa libero interdum nec interdum vel blandit sed nulla ullamcorper <span class="quote-mark">”</span></p>
    <div class="author">
      <div class="avatar" role="img" aria-label="Reviewer portrait"></div>
      <div><div class="author-name">By Author Name</div><div class="author-city">City Location</div></div>
    </div>
  </section>

  <section class="news">
    <div class="news-head">
      <h2>Latest News</h2>
      <div class="news-arrows">
        <svg width="18" height="30" viewBox="0 0 18 30"><polyline points="15,3 3,15 15,27" fill="none" stroke="#555" stroke-width="3"/></svg>
        <svg width="18" height="30" viewBox="0 0 18 30"><polyline points="3,3 15,15 3,27" fill="none" stroke="#555" stroke-width="3"/></svg>
      </div>
    </div>
    <div class="news-row">
      <article class="news-item">
        <div class="news-photo lineup" role="img" aria-label="Photo of a row of parked sports cars under a cloudy sky"></div>
        <h3 class="news-title">News Tittle here</h3>
        <p class="news-text">malesuada nec ultricies sit amet porttitor mattis enim in massa libero</p>
        <p class="read-more">READ MORE</p>
      </article>
      <article class="news-item">
        <div class="news-photo drivers" role="img" aria-label="Photo of two people riding in a car"></div>
        <h3 class="news-title">News Tittle here</h3>
        <p class="news-text">malesuada nec ultricies sit amet porttitor mattis enim in massa libero</p>
        <p class="read-more">READ MORE</p>
      </article>
    </div>
  </section>

  <footer class="site-footer">
    <p>© 2017 Company Name &nbsp;All right reserved</p>
    <p class="footer-links">Term of Use &nbsp;| &nbsp;Privacy Policy</p>
    <div class="social"><span></span><span></span><span></span><span></span></div>
  </footer>
</main>
</body>
</html>
```